Restaurant menu design

I need a menu for a restaurant in Spain.
It has to be bohemian but modern. We need something romantic and elegant.
The restaurant is elegant with good food and an excellent reputation. It is also modern at the same time.
The restaurant is superbly decorated and very chick so we need something "class" to fit in with the surroundings.
The size of the document must be 325 mm in high and 245 mm as a maximum and preferably made in indesign.

Reason: Thank you all for your designs.
So far all your designs are ok but it isn´t what we are looking for. Most of the designs are too loaded, too many colors and too much decoration.

Target Market(s)

Adults of various age groups and different nationalities mostly European.

Industry/Entity Type

Restaurant

Requirements
Must have
• The menu must have two interior pages with the text as in the document attached.It must be easily legible.
Nice to have
• See what kind of menus they use in important restaurants in places like Paris, see what designs are in trend, but Not necessarily doing the same style if it doesn’t fit in with the description above.
Should not have
• Nothing old fashioned.

```html
<!DOCTYPE html>
<html lang="es">
<head>
<meta charset="utf-8">
<title>La Violette – Carta</title>
<link rel="stylesheet" href="https://fonts.googleapis.com/css2?family=Parisienne&family=Tinos:ital@1&display=swap">
<style>
  :root{
    --paper:#ffffff;
    --wood-dark:#4a1208;
    --wood-mid:#7a2410;
    --page-light:#f3c6e8;
    --page-mid:#e6a2d4;
    --page-edge:#d789c3;
    --rim:#f7d9ef;
    --title:#a5212b;
    --ink:#1b1216;
  }
  *{margin:0;padding:0;box-sizing:border-box}
  html,body{width:1200px;height:900px;overflow:hidden;background:var(--paper)}
  .canvas{position:relative;width:1200px;height:900px}
  .spread-art{position:absolute;left:0;top:0}
  .page-column{position:absolute;top:0;text-align:center;color:var(--ink);
    font-family:"Tinos",serif;font-style:italic}
  .page-left{left:0;width:596px}
  .page-right{left:604px;width:596px}
  .section-title{position:absolute;left:0;right:0;font-family:"Parisienne",cursive;
    font-style:normal;font-weight:400;color:var(--title);font-size:26px;line-height:1}
  .dish-list{position:absolute;left:0;right:0;list-style:none;font-size:12.5px}
  .dish-list li{white-space:nowrap}
  .price{font-size:9px;margin-left:12px}
  .entradas .dish-list li,.pescados .dish-list li,.ninos .dish-list li{line-height:17px}
  .carnes .dish-list li,.postres .dish-list li{line-height:18.7px}
  .sauce-line{position:absolute;left:0;right:0;font-size:10px;white-space:nowrap}
  .sauce-line .sauce-label{font-family:"Parisienne",cursive;font-style:normal;color:var(--title);font-size:15px}
  .sauce-line .price{font-size:8px;margin-left:8px}
  .sauce-line .dot{margin:0 6px}
</style>
</head>
<body>
<main class="canvas">
  <svg class="spread-art" width="1200" height="900" viewBox="0 0 1200 900" aria-hidden="true">
    <defs>
      <linearGradient id="wood" x1="0" y1="0" x2="1" y2="0">
        <stop offset="0" stop-color="var(--wood-mid)"/>
        <stop offset="0.25" stop-color="var(--wood-dark)"/>
        <stop offset="0.5" stop-color="var(--wood-mid)"/>
        <stop offset="0.75" stop-color="var(--wood-dark)"/>
        <stop offset="1" stop-color="var(--wood-mid)"/>
      </linearGradient>
      <radialGradient id="pageLeft" cx="0.45" cy="0.45" r="0.7">
        <stop offset="0" stop-color="var(--page-light)"/>
        <stop offset="0.7" stop-color="var(--page-mid)"/>
        <stop offset="1" stop-color="var(--page-edge)"/>
      </radialGradient>
      <radialGradient id="pageRight" cx="0.55" cy="0.45" r="0.7">
        <stop offset="0" stop-color="var(--page-light)"/>
        <stop offset="0.7" stop-color="var(--page-mid)"/>
        <stop offset="1" stop-color="var(--page-edge)"/>
      </radialGradient>
    </defs>
    <rect class="wood-band" x="0" y="45" width="1200" height="800" fill="url(#wood)"/>
    <rect x="0" y="45" width="1200" height="3" fill="var(--page-edge)"/>
    <path class="page-left-sheet" d="M0 118 C120 100 250 135 380 132 C470 130 540 112 598 100 L598 800 C520 795 420 760 300 764 C180 768 90 792 0 790 Z"
      fill="url(#pageLeft)" stroke="var(--rim)" stroke-width="3"/>
    <path class="page-right-sheet" d="M602 100 C660 112 730 130 820 132 C950 135 1080 100 1200 118 L1200 790 C1110 792 1020 768 900 764 C780 760 680 795 602 800 Z"
      fill="url(#pageRight)" stroke="var(--rim)" stroke-width="3"/>
    <rect class="gutter" x="590" y="100" width="20" height="700" fill="var(--page-edge)" opacity="0.35"/>
  </svg>

  <section class="page-column page-left">
    <div class="entradas">
      <h2 class="section-title" style="top:140px">Entradas</h2>
      <ul class="dish-list" style="top:190px">
        <li>Ensalada La Violette. Lechuga, tomate.<span class="price">7,75 €</span></li>
        <li>Ensalada Caprese (Tomate y Mozzarella).<span class="price">7,75 €</span></li>
        <li>Escarola al Queso de Cabra con Bacon.<span class="price">6,75 €</span></li>
        <li>Cocktail de Gambas, Langostinos y Aguacate.<span class="price">7,50 €</span></li>
        <li>La Sopa de Pescado.<span class="price">8,25 €</span></li>
        <li>Crema de Espárragos Trigueros y Calabacín.<span class="price">5,95 €</span></li>
        <li>Carpaccio de Ternera.<span class="price">11,50 €</span></li>
        <li>Carpaccio de Salmón al Eneldo.<span class="price">9,75 €</span></li>
        <li>Carpaccio de Atún.<span class="price">13,95 €</span></li>
        <li>Melón con Jamón Ibérico.<span class="price">9,25 €</span></li>
        <li>Parrillada de Verduras.<span class="price">7,95 €</span></li>
        <li>Parrillada de Verduras Gratinada al Queso de Cabra.<span class="price">8,95 €</span></li>
        <li>Gambas Roja de la Bahía.<span class="price">12,95 €</span></li>
      </ul>
    </div>
    <div class="pescados">
      <h2 class="section-title" style="top:440px">Pescados al Grill</h2>
      <ul class="dish-list" style="top:484px">
        <li>Lubina al Hinojo.<span class="price">15,50 €</span></li>
        <li>Lubina Fileteada y su Salsa Rústica con Berenjena.<span class="price">18,50 €</span></li>
        <li>Filete de Rodaballo y su Salsa de Marisco.<span class="price">17,25 €</span></li>
        <li>Dorada del Mediterráneo.<span class="price">13,95 €</span></li>
        <li>Lenguado al Grill con Hierbas Provenzales.<span class="price">20,75 €</span></li>
        <li>Pieza de Atún Fresco y su Salsa Griega.<span class="price">18,95 €</span></li>
        <li>Lomo de Salmón con Salsa de Frambuesa.<span class="price">11,25 €</span></li>
        <li>Parrillada de Pescado y Marisco.<span class="price">23,505 €</span></li>
      </ul>
    </div>
    <div class="ninos">
      <h2 class="section-title" style="top:676px">Especial Niños</h2>
      <ul class="dish-list" style="top:722px">
        <li>Solomillo Junior, huevo y patatas fritas.<span class="price">6,25 €</span></li>
        <li>Fish &amp; chips.<span class="price">6,25 €</span></li>
      </ul>
    </div>
  </section>

  <section class="page-column page-right">
    <div class="carnes">
      <h2 class="section-title" style="top:140px">Carnes</h2>
      <ul class="dish-list" style="top:188px">
        <li>Pechuga de Pollo “Madame Rose” con Champiñones y Bacon.<span class="price">11,95 €</span></li>
        <li>Chuletas de Cordero.<span class="price">14,50 €</span></li>
        <li>Costillas de Cerdo con Salsa Barbacoa.<span class="price">9,95 €</span></li>
        <li>Paletilla de Cordero Lechal.<span class="price">19,75 €</span></li>
        <li>Le Strogonoff. Finas tiras de Solomillo con su Salsa de Champiñones.<span class="price">15,90 €</span></li>
        <li>Solomillo de Ternera.<span class="price">18,50 €</span></li>
        <li>Solomillo de Ternera a la Ibérica <small>con Jamón Ibérico y Ligera Salsa de Vino Tinto.</small><span class="price">20,75 €</span></li>
        <li>“Hamburger Maison Steak Haché”. <small>Picata de Solomillo de Ternera, Huevo Frito y Patatas Fritas</small><span class="price">14,50 €</span></li>
        <li>Solomillo de Cerdo al Horno con Bacon y su Salsa de Setas.<span class="price">14,25 €</span></li>
        <li>Entrecôte de Ternera.<span class="price">14,75 €</span></li>
        <li>T-Bone Steak de Ternera.<span class="price">16,75 €</span></li>
        <li>Chuletón de Ternera.<span class="price">20,25 €</span></li>
        <li>Parrillada de Carnes y Embutidos.<span class="price">21,50 €</span></li>
      </ul>
      <p class="sauce-line" style="top:456px"><span class="sauce-label">Salsas:</span> Pimienta.<span class="price">2,85 €</span><span class="dot">·</span>Roquefort.<span class="price">2,95 €</span><span class="dot">·</span>Bearnaise.<span class="price">2,95 €</span><span class="dot">·</span>de Champiñones.<span class="price">2,65 €</span></p>
    </div>
    <div class="postres">
      <h2 class="section-title" style="top:528px">Los Postres de la Violette</h2>
      <ul class="dish-list" style="top:570px">
        <li>Frambuesas “La Violette”.<span class="price">6,25 €</span></li>
        <li>Cocktail de Frutas Exóticas.<span class="price">5,25 €</span></li>
        <li>Sorbete de Limón, Coulis de Fresa y Vodka.<span class="price">5,50 €</span></li>
        <li>Pastel de Chocolate Casero con su Salsa de Vainilla.<span class="price">6,25 €</span></li>
        <li>Crême Bruléе.<span class="price">6,25 €</span></li>
        <li>Tarta de Manzana Casera “Tatín” y su Helado de Vainilla.<span class="price">6,95 €</span></li>
        <li>Copa Glaciar Nord.<span class="price">6,75 €</span></li>
        <li>Pera al Chocolate Caliente y Helado de Macadamia.<span class="price">5,95 €</span></li>
        <li>Tarta de Queso con Coulis de Fresa.<span class="price">5,75 €</span></li>
        <li>Nuestra Mousse de Chocolate.<span class="price">5,75 €</span></li>
      </ul>
    </div>
  </section>
</main>
</body>
</html>
```